Web Design Project

Kluvora.com is an online forum for chatting with friends whilst watching TV. We have attached our wireframes, which we would like a design for. The target audience are 11-40 years old.
Please see similar sites (eg Pollent) for inspiration.
Updates

Target Market(s)

11 to 40 year olds, TV viewers

Industry/Entity Type

Tv

Requirements
Must have
• All the pages and elements included in the wireframes.
Nice to have
• Bold graphical elements.

```html
<!DOCTYPE html>
<html lang="en">
<head>
<meta charset="utf-8">
<title>Kluvora – TV Guide</title>
<link rel="stylesheet" href="https://fonts.googleapis.com/css2?family=Montserrat:wght@500;600;700&family=Arimo:wght@400;700&display=swap">
<style>
:root{
  --ad-band:#5d5d5d; --ad-box:#4f4f4f; --ad-text:#8a8a8a;
  --header-top:#3a3a3a; --header-bottom:#050505;
  --page:#f2f2f2; --panel:#ffffff; --panel-head:#dedede; --side:#e8e8e8;
  --time:#d6d6d6; --ink:#111; --muted:#555;
  --teal:#2fbfa9; --navy:#114a55; --berry:#a5445e; --amber:#e3974a;
  --red:#d0141b; --footer:#333333; --footer-text:#ffffff;
  --btn:#3f3f3f; --btn-light:#5b5b5b;
}
*{box-sizing:border-box;margin:0;padding:0}
html,body{width:1200px;height:830px;overflow:hidden}
body{position:relative;background:var(--page);font-family:"Arimo",Arial,sans-serif;color:var(--ink)}
.abs{position:absolute}
.ad-band{left:0;top:0;width:1200px;height:99px;background:var(--ad-band)}
.ad-slot{left:249px;top:6px;width:699px;height:86px;background:var(--ad-box);color:var(--ad-text);font:600 16px "Montserrat",sans-serif;letter-spacing:1px;display:flex;align-items:center;justify-content:center}
.site-header{left:0;top:99px;width:1200px;height:103px;background:linear-gradient(var(--header-top),var(--header-bottom))}
.brand{left:45px;top:138px;color:#fff;font:700 28px "Montserrat",sans-serif;display:flex;align-items:center;gap:8px}
.brand-dot{width:22px;height:22px;border-radius:50%;background:#fff}
.main-nav{left:228px;top:148px;display:flex;color:#fff;font:600 16px "Montserrat",sans-serif}
.main-nav span{padding:0 13px;border-left:1px solid #666;line-height:24px}
.main-nav span:first-child{padding-left:0;border:0}
.btn-settings{left:896px;top:143px;width:108px;height:36px;background:var(--btn);border-radius:3px;color:#fff;font:600 13px "Montserrat",sans-serif;display:flex;align-items:center;justify-content:center;gap:6px}
.btn-login{left:1018px;top:143px;width:159px;height:36px;background:var(--btn-light);border-radius:3px;color:#fff;font:600 13px "Montserrat",sans-serif;display:flex;align-items:center;justify-content:center}
.guide{left:15px;top:219px;width:876px;height:536px;background:var(--panel)}
.guide-head{left:15px;top:219px;width:876px;height:55px;background:var(--panel-head)}
.guide-title{left:35px;top:238px;font:700 15px "Arimo",sans-serif}
.search{left:653px;top:235px;width:226px;height:24px;border-radius:12px;background:#c9c9c9;font-size:10px;color:#777;display:flex;align-items:center;padding-left:10px;gap:8px}
.time{top:288px;width:121px;height:15px;background:var(--time);font-size:10px;padding-left:7px;line-height:15px}
.channel{left:34px;width:57px;height:40px;border-radius:2px;color:#fff;font:700 11px "Arimo",sans-serif;display:flex;align-items:center;justify-content:center;text-align:center;line-height:12px}
.ch-red{background:var(--red)}.ch-black{background:#111}.ch-plum{background:#5c1f4c}.ch-green{background:#0d6b5a}
.show{height:40px;border-radius:3px;color:#fff;font:700 11.5px "Arimo",sans-serif;display:flex;align-items:center;padding-left:12px;white-space:nowrap;overflow:hidden}
.teal{background:var(--teal)}.navy{background:var(--navy)}.berry{background:var(--berry)}.amber{background:var(--amber)}
.scroll-v{left:880px;top:280px;width:9px;height:470px;background:#f0f0f0}
.scroll-v i{position:absolute;left:1px;top:0;width:7px;height:136px;background:#c8c8c8;border-radius:4px}
.scroll-h{left:21px;top:744px;width:646px;height:8px;background:#c8c8c8;border-radius:4px}
.side{left:900px;top:219px;width:286px;height:536px;background:var(--side)}
.side-head{left:900px;top:219px;width:286px;height:55px;background:#dcdcdc}
.side-logo{left:910px;top:232px;width:48px;height:30px;background:var(--red);color:#fff;font:700 10px "Arimo",sans-serif;display:flex;align-items:center;justify-content:center}
.side-title{left:965px;top:231px;font:700 15px "Arimo",sans-serif}
.side-time{left:965px;top:250px;font-size:12px}
.side-photo{left:916px;top:286px;width:241px;height:112px;background:linear-gradient(90deg,#8a5a45,#4a3a34 55%,#2a2526)}
.side-scroll{left:1173px;top:280px;width:8px;height:70px;background:#c8c8c8;border-radius:4px}
.about{left:916px;top:409px;width:240px}
.about h2{font:700 16px "Arimo",sans-serif;margin-bottom:4px}
.about p{font-size:11.5px;line-height:17px}
.crew{left:916px;top:530px;width:245px;font-size:11.5px}
.crew h2{font:700 16px "Arimo",sans-serif;margin-bottom:3px}
.crew dl{display:grid;grid-template-columns:70px 1fr;row-gap:2px;line-height:15.5px}
.crew dl.prod{grid-template-columns:119px 1fr;margin-top:11px}
.crew dl.prod dt{font-weight:700}
.join{left:968px;top:705px;width:155px;height:26px;border-radius:13px;background:#000;color:#fff;font:700 11.5px "Montserrat",sans-serif;display:flex;align-items:center;justify-content:center}
.site-footer{left:0;top:773px;width:1200px;height:57px;background:var(--footer);color:var(--footer-text);display:flex;align-items:center}
.copyright{position:absolute;left:36px;font:600 8.5px "Arimo",sans-serif}
.footer-nav{position:absolute;left:145px;display:flex;font:600 8.5px "Arimo",sans-serif}
.footer-nav span{padding:0 9px;border-left:1px solid #aaa;line-height:9px}
.footer-nav span:first-child{border:0}
.stay{position:absolute;left:996px;font:700 12px "Montserrat",sans-serif}
.social{position:absolute;left:1080px;display:flex;gap:8px;font:600 10px "Arimo",sans-serif;color:#bbb}
</style>
</head>
<body>
<div class="abs ad-band"></div>
<div class="abs ad-slot">728X90 AD SPACE</div>

<header class="abs site-header"></header>
<div class="abs brand"><span class="brand-dot"></span>Kluvora</div>
<nav class="abs main-nav"><span>HOME</span><span>MY CONVERSATIONS</span></nav>
<div class="abs btn-settings">
  <svg width="16" height="16" viewBox="0 0 16 16" aria-hidden="true"><g fill="#888"><circle cx="8" cy="8" r="5"/><rect x="7" y="0" width="2" height="16"/><rect x="0" y="7" width="16" height="2"/><rect x="7" y="0" width="2" height="16" transform="rotate(45 8 8)"/><rect x="7" y="0" width="2" height="16" transform="rotate(-45 8 8)"/></g><circle cx="8" cy="8" r="2" fill="#3f3f3f"/></svg>SETTINGS</div>
<div class="abs btn-login">LOGIN TO KLUVORA</div>

<main>
<section class="abs guide"></section>
<div class="abs guide-head"></div>
<div class="abs guide-title">Select a program to join the conversation or use the search bar</div>
<div class="abs search"><svg width="12" height="12" viewBox="0 0 12 12" aria-hidden="true"><circle cx="7" cy="5" r="3.5" fill="none" stroke="#666" stroke-width="1.5"/><line x1="4.5" y1="7.5" x2="1" y2="11" stroke="#666" stroke-width="2"/></svg>Search Programming</div>

<div class="abs time" style="left:100px">9:00</div>
<div class="abs time" style="left:228px">9:30</div>
<div class="abs time" style="left:353px">10:00</div>
<div class="abs time" style="left:481px">10:30</div>
<div class="abs time" style="left:609px">11:00</div>
<div class="abs time" style="left:734px">11:30</div>

<!-- row 1 -->
<div class="abs channel ch-red" style="top:315px">Vela One</div>
<div class="abs show teal" style="top:315px;left:99px;width:122px">Program Name</div>
<div class="abs show teal" style="top:315px;left:228px;width:231px">Program Name</div>
<div class="abs show teal" style="top:315px;left:466px;width:122px">Program Name</div>
<div class="abs show teal" style="top:315px;left:593px;width:262px">Program Name</div>
<!-- row 2 -->
<div class="abs channel ch-black" style="top:361px">Norv 1</div>
<div class="abs show navy" style="top:361px;left:99px;width:122px">Program Name</div>
<div class="abs show navy" style="top:361px;left:228px;width:120px">Program Name</div>
<div class="abs show navy" style="top:361px;left:355px;width:122px">Program Name</div>
<div class="abs show navy" style="top:361px;left:483px;width:160px">Program Name</div>
<div class="abs show navy" style="top:361px;left:651px;width:204px">Program Name</div>
<!-- row 3 -->
<div class="abs channel ch-plum" style="top:407px">Vela Three</div>
<div class="abs show berry" style="top:407px;left:99px;width:250px">Program Name</div>
<div class="abs show berry" style="top:407px;left:355px;width:232px">Program Name</div>
<div class="abs show berry" style="top:407px;left:593px;width:262px">Program Name</div>
<!-- row 4 -->
<div class="abs channel ch-black" style="top:453px">Norv 3</div>
<div class="abs show amber" style="top:453px;left:99px;width:132px">Program Name</div>
<div class="abs show amber" style="top:453px;left:237px;width:179px">Program Name</div>
<div class="abs show amber" style="top:453px;left:421px;width:78px">Program...</div>
<div class="abs show amber" style="top:453px;left:506px;width:153px">Program Name</div>
<div class="abs show amber" style="top:453px;left:665px;width:190px">Program Name</div>
<!-- row 5 -->
<div class="abs channel ch-black" style="top:499px">Norv 4</div>
<div class="abs show teal" style="top:499px;left:99px;width:201px">Program Name</div>
<div class="abs show teal" style="top:499px;left:305px;width:154px">Program Name</div>
<div class="abs show teal" style="top:499px;left:466px;width:122px">Program Name</div>
<div class="abs show teal" style="top:499px;left:593px;width:262px">Program Name</div>
<!-- row 6 -->
<div class="abs channel ch-black" style="top:545px">Vela Four</div>
<div class="abs show navy" style="top:545px;left:99px;width:122px">Program Name</div>
<div class="abs show navy" style="top:545px;left:228px;width:120px">Program Name</div>
<div class="abs show navy" style="top:545px;left:355px;width:122px">Program Name</div>
<div class="abs show navy" style="top:545px;left:483px;width:160px">Program Name</div>
<div class="abs show navy" style="top:545px;left:651px;width:204px">Program Name</div>
<!-- row 7 -->
<div class="abs channel ch-green" style="top:591px">Vela Two</div>
<div class="abs show berry" style="top:591px;left:99px;width:250px">Program Name</div>
<div class="abs show berry" style="top:591px;left:355px;width:232px">Program Name</div>
<div class="abs show berry" style="top:591px;left:593px;width:262px">Program Name</div>
<!-- row 8 -->
<div class="abs channel ch-red" style="top:637px">Vela One</div>
<div class="abs show amber" style="top:637px;left:99px;width:132px">Program Name</div>
<div class="abs show amber" style="top:637px;left:237px;width:179px">Program Name</div>
<div class="abs show amber" style="top:637px;left:421px;width:78px">Program...</div>
<div class="abs show amber" style="top:637px;left:506px;width:153px">Program Name</div>
<div class="abs show amber" style="top:637px;left:665px;width:190px">Program Name</div>
<!-- row 9 -->
<div class="abs channel ch-red" style="top:683px">Vela One</div>
<div class="abs show teal" style="top:683px;left:99px;width:122px">Program Name</div>
<div class="abs show teal" style="top:683px;left:228px;width:231px">Program Name</div>
<div class="abs show teal" style="top:683px;left:466px;width:122px">Program Name</div>
<div class="abs show teal" style="top:683px;left:593px;width:262px">Program Name</div>

<div class="abs scroll-v"><i></i></div>
<div class="abs scroll-h"></div>

<aside>
<div class="abs side"></div>
<div class="abs side-head"></div>
<div class="abs side-logo">Vela One</div>
<div class="abs side-title">Casewatch Tour</div>
<div class="abs side-time">9:15 am - 10 am</div>
<div class="abs side-photo" role="img" aria-label="Photo of the programme presenter standing by a brick wall with a security camera"></div>
<div class="abs side-scroll"></div>
<div class="abs about">
  <h2>About This Program</h2>
  <p>14/20. South Wales police appeal for information in a bid to catch the men who attacked a pensioner, and reporter Mara Hollis interviews the parents of murdered teenager Leanne.</p>
</div>
<div class="abs crew">
  <h2>Cast and Crew</h2>
  <dl><dt>Reporter</dt><dd>Mara Hollis</dd><dt>Reporter</dt><dd>Tom Pryce</dd><dt>Presenter</dt><dd>Jas Malden</dd></dl>
  <dl class="prod"><dt>Executive Producer</dt><dd>Helen Carrow</dd><dt>Series Producer</dt><dd>Ffion Barlow</dd></dl>
</div>
<div class="abs join">JOIN CONVERSATION</div>
</aside>
</main>

<footer class="abs site-footer">
  <span class="copyright">© KLUVORA 2012</span>
  <nav class="footer-nav"><span>HOME</span><span>HELP</span><span>PRESS</span><span>ABOUT US</span><span>CONTACT US</span><span>PRIVACY POLICY</span><span>TERMS &amp; CONDITIONS</span><span>STARS</span><span>JOBS</span></nav>
  <span class="stay">STAY TUNED</span>
  <span class="social"><span>Facet</span><span>Chirp</span><span>Tubely</span></span>
</footer>
</body>
</html>
```